12 page New Church Launch Booklet

I have a 12 page 8.5x11 Mock-up of a Launch booklet I need to get done and made ready to be sent to Pressvale.com for printing. I have uploaded the 12 pages and the content that I need. I need to have this designed from scratch while being inspired by the mock-up. I am open to new concepts and design ideas from the designer. I would like to use some of the pictures that are included in the mock-up but if there are other options that will work better i am open to that.

Target Market(s)

Churches who support church plants and individuals who may be interested in joining the launch team.

Font styles to use
Serif

Colors

Designer to choose colors to be used in the design.

Requirements
Must have
• I have uploaded a mock-up. i just want something that will be appealing to the eye.

```html
<!DOCTYPE html>
<html lang="en">
<head>
<meta charset="utf-8">
<title>Kindle Church Launch Booklet</title>
<link href="https://fonts.googleapis.com/css2?family=Montserrat:wght@800;900&family=Poppins:wght@400;500;600&family=Playball&display=swap" rel="stylesheet">
<style>
:root{
  --bg:#c9c9cb;
  --black:#0d0d0d;
  --ink:#2a2a2a;
  --white:#ffffff;
  --paper:#f7f7f6;
  --orange:#ee8a1c;
  --amber:#f4a225;
  --red:#d9261f;
  --flame:#e2461f;
}
*{box-sizing:border-box;margin:0;padding:0}
html,body{width:754px;height:1200px;overflow:hidden;background:var(--bg)}
body{position:relative;font-family:'Poppins',sans-serif;color:var(--ink)}
.spread{position:absolute;left:87px;width:580px;height:375px;display:flex;box-shadow:0 6px 16px rgba(0,0,0,.28)}
.spread--cover{top:18px}
.spread--bio{top:411px}
.spread--story{top:804px}
.page{position:relative;width:290px;height:375px;overflow:hidden}
.spine{position:absolute;left:285px;top:0;width:10px;height:375px;background:linear-gradient(90deg,rgba(0,0,0,0),rgba(0,0,0,.18),rgba(0,0,0,0));pointer-events:none;z-index:5}
.photo{position:absolute}
.brand-name{font-family:'Poppins',sans-serif;font-weight:500;color:var(--white);white-space:nowrap}

/* cover */
.cover-back{background:var(--black)}
.info-panel{position:absolute;left:0;top:0;width:130px;height:375px;background:linear-gradient(180deg,var(--red) 0%,var(--flame) 25%,var(--orange) 65%,var(--amber) 100%)}
.info-panel .brand-name{position:absolute;left:14px;top:182px;font-size:14px}
.contact{position:absolute;left:14px;top:222px;width:112px;color:var(--white);font-size:6px;line-height:1.5}
.contact h3{font-weight:600;font-size:6.6px;letter-spacing:.3px}
.social{position:absolute;left:14px;top:285px;display:flex;gap:5px}
.social span{width:11px;height:11px;border-radius:50%;background:rgba(255,255,255,.9)}
.cover-photo{left:160px;top:0;width:420px;height:375px;
  background:
    radial-gradient(circle at 64% 34%,rgba(196,120,70,.75) 0,rgba(196,120,70,0) 70px),
    radial-gradient(circle at 40% 30%,rgba(150,80,45,.55) 0,rgba(150,80,45,0) 60px),
    radial-gradient(circle at 85% 22%,rgba(170,110,80,.45) 0,rgba(170,110,80,0) 55px),
    radial-gradient(circle at 30% 65%,rgba(120,60,35,.45) 0,rgba(120,60,35,0) 70px),
    linear-gradient(180deg,#2a1810 0%,#1a0f0a 55%,#090706 80%,#050505 100%)}
.cover-fade{position:absolute;left:130px;top:0;width:100px;height:375px;background:linear-gradient(90deg,var(--black),rgba(13,13,13,0))}
.cover-fade--bottom{position:absolute;left:130px;top:220px;width:450px;height:155px;background:linear-gradient(180deg,rgba(5,5,5,0),rgba(5,5,5,.95))}
.front-overlay{position:absolute;left:290px;top:0;width:290px;height:375px;z-index:2}
.front-overlay .brand-name{position:absolute;left:0;width:290px;text-align:center;top:34px;font-size:26px}
.launch{position:absolute;left:0;width:290px;text-align:center}
.launch--script{top:240px;font-family:'Playball',cursive;color:var(--white);font-size:18px}
.launch--date{top:264px;font-family:'Montserrat',sans-serif;font-weight:900;font-size:21px;color:var(--orange)}
.tagline{position:absolute;left:42px;top:304px;width:206px;border:1px solid rgba(255,255,255,.8);color:var(--white);font-size:6.6px;letter-spacing:1.6px;text-align:center;padding:3px 0}

/* bio */
.bio-left,.bio-right{background:var(--paper)}
.portrait{left:0;top:0;width:118px;height:375px;
  background:
    radial-gradient(ellipse 50px 150px at 55% 62%,rgba(20,12,6,.85) 0,rgba(20,12,6,0) 100%),
    linear-gradient(160deg,#d48a2c 0%,#a9621e 40%,#6b3a12 75%,#3a1f0c 100%)}
.bio-text{position:absolute;left:132px;top:32px;width:146px}
.bio-text h1{font-family:'Montserrat',sans-serif;font-weight:800;font-size:16px;color:var(--black);letter-spacing:.3px}
.role{color:var(--orange);font-size:7px;font-weight:500;letter-spacing:.4px;margin:2px 0 10px}
.body{font-size:5.7px;line-height:1.55;color:var(--ink);text-align:justify}
.section-title{color:var(--orange);font-weight:600;font-size:7px;margin:12px 0 5px}
.checks{list-style:none}
.checks li{position:relative;padding-left:12px;font-size:6px;line-height:1.4;margin-bottom:6px;color:var(--ink)}
.checks svg{position:absolute;left:0;top:1px;width:7px;height:7px}
.connect{position:absolute;left:18px;top:38px;width:150px}
.connect h2{font-family:'Montserrat',sans-serif;font-weight:900;color:var(--orange);font-size:14px;line-height:1.1;margin-bottom:10px}
.meeting-photo{left:22px;top:250px;width:126px;height:70px;
  background:
    radial-gradient(circle at 78% 55%,rgba(230,110,30,.8) 0,rgba(230,110,30,0) 10px),
    linear-gradient(90deg,#d9d4cc 0%,#b7aa98 35%,#5a4a3c 70%,#2d241d 100%)}
.meeting-bar{position:absolute;left:148px;top:244px;width:5px;height:62px;background:var(--orange)}
.couple-photo{left:176px;top:0;width:114px;height:375px;
  background:
    radial-gradient(ellipse 60px 120px at 55% 45%,rgba(40,40,40,.6) 0,rgba(40,40,40,0) 100%),
    linear-gradient(180deg,#9a9a9a 0%,#6a6a6a 40%,#3a3a3a 75%,#1e1e1e 100%)}

/* story */
.story-left{background:var(--black)}
.street-photo{left:0;top:0;width:290px;height:118px;background:linear-gradient(180deg,#e8743a 0%,#c2542a 30%,#6d2c14 65%,#2a140b 85%,var(--black) 100%)}
.story-title{position:absolute;right:24px;top:20px;font-family:'Montserrat',sans-serif;font-weight:900;font-size:17px;color:var(--white);letter-spacing:.5px}
.story-body{position:absolute;left:18px;width:254px;color:#eee;font-size:5.6px;line-height:1.55;text-align:justify}
.story-body--one{top:124px}
.subhead{position:absolute;left:18px;top:220px;font-family:'Playball',cursive;font-size:15px;color:var(--orange)}
.story-body--two{top:242px}
.story-left .brand-name{position:absolute;left:18px;top:344px;font-size:12px}
.rule{position:absolute;left:112px;top:353px;width:160px;height:1px;background:rgba(255,255,255,.35)}
.story-right{background:linear-gradient(180deg,var(--red) 25%,var(--flame) 50%,var(--orange) 80%,var(--amber) 100%)}
.stage-photo{left:0;top:0;width:290px;height:118px;
  background:
    radial-gradient(ellipse 70px 30px at 60% 38%,rgba(160,200,90,.85) 0,rgba(160,200,90,0) 100%),
    radial-gradient(ellipse 18px 40px at 68% 60%,rgba(140,70,40,.7) 0,rgba(140,70,40,0) 100%),
    linear-gradient(180deg,#141a28 0%,#0e121c 60%,#0a0c12 100%)}
.quote-mark{position:absolute;left:18px;top:108px;width:22px;height:22px;background:var(--black);border:1.5px solid var(--white);color:var(--white);font-family:'Montserrat',sans-serif;font-weight:900;font-size:18px;line-height:24px;text-align:center}
.pull-quote{position:absolute;left:18px;top:136px;width:256px;font-family:'Montserrat',sans-serif;font-weight:800;color:var(--white);font-size:8.6px;line-height:1.25}
.quote-name{position:absolute;left:18px;top:172px;font-family:'Montserrat',sans-serif;font-weight:900;color:var(--white);font-size:12px}
.story-body--three{top:194px;color:var(--white);width:254px}
.story-right .brand-name{position:absolute;right:16px;top:344px;font-size:11px}
</style>
</head>
<body>

<section class="spread spread--cover">
  <div class="page cover-back">
    <div class="info-panel">
      <div class="brand-name">Kindle Church</div>
      <div class="contact">
        <h3>FOR MORE INFORMATION</h3>
        Email: hello@kindlechurch.org<br>
        Phone: 555-014-2290 or visit us<br>
        kindlechurch.org
      </div>
      <div class="social" aria-label="Social links"><span></span><span></span><span></span><span></span></div>
    </div>
  </div>
  <div class="page cover-front"></div>
  <div class="photo cover-photo" role="img" aria-label="Worshippers raising hands, one holding up a Bible"></div>
  <div class="cover-fade"></div>
  <div class="cover-fade--bottom"></div>
  <div class="front-overlay">
    <div class="brand-name">Kindle Church</div>
    <div class="launch launch--script">Launching</div>
    <div class="launch launch--date">APRIL 12, 2020</div>
    <div class="tagline">" A Multi-ethnic church planting church"</div>
  </div>
  <div class="spine"></div>
</section>

<section class="spread spread--bio">
  <div class="page bio-left">
    <div class="photo portrait" role="img" aria-label="Portrait of the church planter standing by a brick wall"></div>
    <div class="bio-text">
      <h1>I am MARCUS.</h1>
      <p class="role">CHURCH PLANTER</p>
      <p class="body">Marcus Dale was born and raised as a preacher's kid in the central city of Riverton. As a youth, he was involved with gangs and by the age of 22, was a successful drug dealer. After a near death experience, he gave his life to Jesus and would later become an ordained minister. In 2005, he planted his first church in the central city of Riverton. In 2016, he led the launch of a north side multi-ethnic ministry initiative for Agora church. He and his wife Renee are the proud parents of 5 adult children and the proud grandparents of 10.</p>
      <p class="section-title">EDUCATION</p>
      <ul class="checks">
        <li><svg viewBox="0 0 10 10"><circle cx="5" cy="5" r="4.2" fill="none" stroke="#ee8a1c" stroke-width="1"/><path d="M3 5.2l1.5 1.5L7.2 3.8" fill="none" stroke="#ee8a1c" stroke-width="1.1"/></svg>B.A. in business from Westbrook University.</li>
        <li><svg viewBox="0 0 10 10"><circle cx="5" cy="5" r="4.2" fill="none" stroke="#ee8a1c" stroke-width="1"/><path d="M3 5.2l1.5 1.5L7.2 3.8" fill="none" stroke="#ee8a1c" stroke-width="1.1"/></svg>M.A. in Christian Ministry from Harbor Baptist Theological Seminary.</li>
        <li><svg viewBox="0 0 10 10"><circle cx="5" cy="5" r="4.2" fill="none" stroke="#ee8a1c" stroke-width="1"/><path d="M3 5.2l1.5 1.5L7.2 3.8" fill="none" stroke="#ee8a1c" stroke-width="1.1"/></svg>Ed. D in Organizational Leadership (ABD) from Red Mesa University.</li>
      </ul>
    </div>
  </div>
  <div class="page bio-right">
    <div class="connect">
      <h2>COMMUNITY<br>CONNECTION</h2>
      <ul class="checks">
        <li><svg viewBox="0 0 10 10"><circle cx="5" cy="5" r="4.2" fill="none" stroke="#ee8a1c" stroke-width="1"/><path d="M3 5.2l1.5 1.5L7.2 3.8" fill="none" stroke="#ee8a1c" stroke-width="1.1"/></svg>Board member of Common Ground Depot and Hands of Hope Alliance</li>
        <li><svg viewBox="0 0 10 10"><circle cx="5" cy="5" r="4.2" fill="none" stroke="#ee8a1c" stroke-width="1"/><path d="M3 5.2l1.5 1.5L7.2 3.8" fill="none" stroke="#ee8a1c" stroke-width="1.1"/></svg>Board member of Crestview High School</li>
        <li><svg viewBox="0 0 10 10"><circle cx="5" cy="5" r="4.2" fill="none" stroke="#ee8a1c" stroke-width="1"/><path d="M3 5.2l1.5 1.5L7.2 3.8" fill="none" stroke="#ee8a1c" stroke-width="1.1"/></svg>Member of Steering Council of Meridian Health Care</li>
        <li><svg viewBox="0 0 10 10"><circle cx="5" cy="5" r="4.2" fill="none" stroke="#ee8a1c" stroke-width="1"/><path d="M3 5.2l1.5 1.5L7.2 3.8" fill="none" stroke="#ee8a1c" stroke-width="1.1"/></svg>Founder and president of Neighbor Link, a neighborhood development organization</li>
        <li><svg viewBox="0 0 10 10"><circle cx="5" cy="5" r="4.2" fill="none" stroke="#ee8a1c" stroke-width="1"/><path d="M3 5.2l1.5 1.5L7.2 3.8" fill="none" stroke="#ee8a1c" stroke-width="1.1"/></svg>President of the Riverton Covenant, a group of multi-ethnic pastors from the region who stand as one in promoting racial unity within the body of Christ.</li>
      </ul>
    </div>
    <div class="photo couple-photo" role="img" aria-label="Black and white photo of the planter and his wife"></div>
    <div class="photo meeting-photo" role="img" aria-label="Two men talking over coffee at a table"></div>
    <div class="meeting-bar"></div>
  </div>
  <div class="spine"></div>
</section>

<section class="spread spread--story">
  <div class="page story-left">
    <div class="photo street-photo" role="img" aria-label="City street of houses at sunset"></div>
    <h2 class="story-title">MY STORY</h2>
    <p class="story-body story-body--one">In spite of being a pastor's kid, I felt as if I was doomed to hell. I never understood why I had to beg God for acceptance, so I gave up and turned to the streets of Riverton. As a successful drug dealer, my peers more than accepted me. I wore the best clothes, drove the best cars, made a ton of money, and simply purchased acceptance and validation from others. Nevertheless, my lavish lifestyle also made me a target. I was robbed three separate times, but it wasn't until the last robbery at gunpoint that I truly began considering life after death. As the gunmen demanded I kneel down, I figured I only had enough time left to ask God to forgive me, which I did. Surprised I was still alive, I then promised God if he got me out of that particular situation, that I would change my life. In a strange twist of fate, the gunmen did not pull the trigger and instead demanded money.</p>
    <div class="subhead">Spared by God</div>
    <p class="story-body story-body--two">All in one swoop, I flipped my body off the porch while landing on my shoeless feet. While there is no reasonable explanation of how that was possible, God not only heard my plea but spared my life that day. I was forever changed! From that day forward, I was determined to keep my vow to the Lord. I completely turned away from my life as a drug dealer, and took a job working as a delivery driver for a pharmaceutical company making $7.50 an hour. How ironic is that? I was still delivering drugs but this time it was legit and for a lot less money. This was my first life lesson in humility! Consequently, a young White guy (my boss) took a keen interest in me and began teaching me the business. He brought me into the warehouse, and from there, into the front office.</p>
    <div class="brand-name">Kindle Church</div>
    <div class="rule"></div>
  </div>
  <div class="page story-right">
    <div class="photo stage-photo" role="img" aria-label="Pastor preaching on a stage beside a lit cross and screen"></div>
    <div class="quote-mark">“</div>
    <p class="pull-quote">I VALUE MULTI-ETHNIC MINISTRY BECAUSE I AM THE PRODUCT OF WHAT CAN HAPPEN THROUGH MULTI-ETHNIC RELATIONSHIPS.</p>
    <p class="quote-name">MARCUS DALE</p>
    <p class="story-body story-body--three">I had worked my way up to the top of that branch. A couple of months later, I was promoted to our corporate office in Dunmore, MS. Unbelievably, in a period of 18 months, I had gone from being a street thug dope dealer to running 13 branches nationwide; albeit, with no college education. By this time, I knew God was at work in my life. Soon after arriving in Dunmore, an older White gentleman knocked at my door. He said he wanted to share the Gospel. I remember him asking me "if you were to die tonight and sat at God's door, what would you say to him in an effort to get in?" I said something along the lines of my good outweighing my bad. However, he informed me that salvation had nothing to do with what I had done in life. He then shared with me Romans 10:9, which I had never heard. That night, I tossed and turned wondering how that scripture could be true in spite of all my imperfections. Tears flowed when it finally hit me. Ironically, the two most important life moments came through multi-ethnic interaction. I value multi-ethnic ministry because I am the product of what can happen through multi-ethnic relationships.</p>
    <div class="brand-name">Kindle Church</div>
  </div>
  <div class="spine"></div>
</section>

</body>
</html>
```